Design website for toyshop

I am looking for a modular web design for my company sells toys for children 1 to 12 years. The name is "Delvik". In this site you could show a large catalog of different brands such as Crane-Dowell, Plunex, TIDDAMUN, VORQUIN, BRUK, Celane, Fast Gears.
Each product should have a space to add a short description (with some examples is sufficient). Be creative and original.
The logo is in other contest
https://www.taskorvo.net/contest/Design-a-logo-and-bussiness-card-for-toyshop-62049.html

Examples what we are looking:
http://www.brindlecrate.net/
http://www.pelumbo.es/home/index.jsp?categoryId=8160947
http://www.quarnely.com/cp/toys/6058
http://www.vexori.com/

```html
<!DOCTYPE html>
<html lang="en">
<head>
<meta charset="utf-8">
<title>Delvik – Toy Shop</title>
<link href="https://fonts.googleapis.com/css2?family=Open+Sans:wght@400;600;700&family=Fredoka:wght@500&display=swap" rel="stylesheet">
<style>
:root{
  --sky-top:#3fbbe8;
  --sky-bottom:#e9f7fd;
  --white:#ffffff;
  --text:#555b61;
  --link-blue:#2f8fd6;
  --price-green:#7bb321;
  --orange:#ff7a12;
  --orange-dark:#f26a00;
  --red:#f2491d;
  --yellow:#f7b21b;
  --green:#8cc027;
  --teal:#129bb4;
  --purple:#7a3aa9;
  --navy:#1d4f87;
  --footer-blue:#0d9fdc;
  --footer-line:#8fd6f3;
  --grey:#f1f1f1;
}
*{box-sizing:border-box;margin:0;padding:0}
html,body{width:1200px;height:1092px;overflow:hidden}
body{
  position:relative;
  font-family:"Open Sans",Arial,sans-serif;
  color:var(--text);
  background:linear-gradient(180deg,var(--sky-top) 0%,#63c8ee 45%,var(--sky-bottom) 80%,#ffffff 100%);
}
.abs{position:absolute}

/* header */
.brand{left:280px;top:28px;display:flex;align-items:center;gap:12px}
.brand-dot{width:54px;height:54px;border-radius:50%;background:var(--yellow)}
.brand-name{font-weight:700;font-size:48px;color:var(--orange);letter-spacing:1px;line-height:1}
.top-links{left:729px;top:31px;width:196px;display:flex;justify-content:space-between;font-size:8px;color:var(--white)}
.top-rule{left:729px;top:52px;width:196px;border-top:1px dotted rgba(255,255,255,.85)}
.cart{left:806px;top:61px;display:flex;align-items:center;gap:6px;font-size:8px;color:var(--white)}
.cart b{font-weight:700;font-size:9px}

.nav{left:477px;top:117px;height:37px;display:flex}
.nav a{display:flex;align-items:center;justify-content:center;height:37px;color:var(--white);font-size:14px;text-decoration:none;text-transform:uppercase}
.nav .home{width:60px;background:var(--red)}
.nav .about{width:67px;background:var(--orange)}
.nav .store{width:66px;background:var(--yellow)}
.nav .featured{width:90px;background:var(--green)}
.nav .news{width:57px;background:var(--teal)}
.nav .contacts{width:95px;background:var(--purple);border-radius:0 6px 0 0}

/* main panel */
.panel{left:276px;top:153px;width:648px;height:730px;background:var(--white);border-radius:6px 6px 0 0}

.slider{left:264px;top:177px;width:448px;height:252px;background:linear-gradient(135deg,#e9e2d6 0%,#c7b9a6 40%,#3a3a38 62%,#2f302f 100%)}
.slider-stripe{left:264px;top:177px;width:448px;height:30px;background:linear-gradient(90deg,#8dc63f,#b4d96b)}
.slider-arrow{width:20px;height:20px;border-radius:50%;background:rgba(90,90,90,.75);display:flex;align-items:center;justify-content:center;top:293px}
.fold{width:0;height:0;top:429px;border-top:10px solid var(--navy)}
.fold.left{left:264px;border-left:12px solid transparent}
.fold.right{left:924px;border-right:12px solid transparent}

.search{left:712px;top:177px;width:224px;height:252px;background:var(--orange);color:var(--white)}
.search h2{position:absolute;left:0;top:14px;width:100%;text-align:center;font-family:"Fredoka",sans-serif;font-weight:500;font-size:17px}
.select{position:absolute;left:13px;width:198px;height:22px;background:var(--white);border-radius:2px;font-size:9px;color:#777;padding:5px 8px}
.select::after{content:"⇕";position:absolute;right:6px;top:4px;color:#444;font-size:10px}
.gender{position:absolute;left:0;top:69px;width:100%;display:flex;justify-content:center;gap:10px;font-size:12px;font-weight:600}
.gender span{display:flex;align-items:center;gap:3px}
.ticks{position:absolute;left:13px;top:94px;width:198px;display:flex;justify-content:space-between;font-size:8px}
.range{position:absolute;left:13px;top:121px;width:198px;height:16px;background:#e24d2c;border:1px solid #fff;border-radius:2px}
.knob{position:absolute;top:-2px;width:16px;height:18px;background:var(--white);border-radius:2px;box-shadow:0 0 2px rgba(0,0,0,.4)}
.range-val{position:absolute;left:0;top:145px;width:100%;text-align:center;font-size:12px;font-weight:700}
.sep{position:absolute;left:13px;width:198px;border-top:1px solid rgba(255,255,255,.7)}
.submit{position:absolute;left:80px;top:213px;width:64px;height:22px;background:var(--purple);font-size:9px;display:flex;align-items:center;justify-content:center}

/* products */
.section-title{font-size:13px;color:var(--link-blue);text-transform:uppercase}
.product{width:147px}
.product-img{width:147px;height:145px;background:linear-gradient(180deg,#ffffff 0%,#eef4f8 60%,#dfe8ee 100%);border-bottom:1px solid #e2e2e2}
.product-title{margin-top:18px;font-size:9px;font-weight:700;color:var(--link-blue)}
.product-desc{margin-top:6px;font-size:8px;line-height:11px;color:#777}
.product-buy{margin-top:10px;display:flex;align-items:center;gap:10px}
.price{font-size:13px;color:var(--price-green)}
.to-cart{height:21px;padding:0 7px;background:var(--orange-dark);color:var(--white);font-size:8.5px;display:flex;align-items:center}

/* brands */
.brand-tile{top:776px;width:86px;height:84px;display:flex;align-items:center;justify-content:center;font-weight:700}
.brand-tile.plunex{background:var(--teal);color:var(--white);font-size:17px}
.brand-tile.bruk{background:#ef3e63;color:var(--white);font-size:20px}
.brand-tile.crane{background:var(--white);color:#1f4f9c;font-size:12px}
.brand-arrow{top:806px;width:20px;height:20px;border-radius:50%;background:rgba(90,90,90,.7);display:flex;align-items:center;justify-content:center}

/* footer */
.footer{left:276px;top:883px;width:648px;height:149px;background:var(--footer-blue);color:var(--white)}
.foot-col{position:absolute;top:24px;width:147px}
.foot-col h3{font-size:10px;font-weight:700;text-transform:uppercase;margin-bottom:8px}
.foot-col li{list-style:none;font-size:8px;height:20px;padding-top:2px;border-bottom:1px dotted var(--footer-line);margin-bottom:0}
.social{position:absolute;top:28px;left:497px;display:flex;gap:7px}
.social span{width:38px;height:38px;border-radius:6px;display:flex;align-items:center;justify-content:center;font-size:7px;font-weight:700;color:var(--white)}
.social .chirply{background:#2db8f0;border:2px solid #fff}
.social .friendo{background:#2f5ea8;border:2px solid #fff}
.social .vidlane{background:#ffffff;color:#d62c2c}
.bottom{left:276px;top:1032px;width:648px;height:60px;background:var(--grey);text-align:center;font-size:8px;color:#666;padding-top:40px}
</style>
</head>
<body>

<header>
  <div class="abs brand"><span class="brand-dot"></span><span class="brand-name">Delvik</span></div>
  <nav class="abs top-links"><span>My Account</span><span>Delivery</span><span>Checkout</span><span>Register</span><span>Login</span></nav>
  <div class="abs top-rule"></div>
  <div class="abs cart">
    <svg width="20" height="16" viewBox="0 0 20 16"><path d="M1 2h3l2 8h10l2-6H5" fill="none" stroke="#8cc027" stroke-width="2"/><circle cx="8" cy="13.5" r="1.6" fill="#8cc027"/><circle cx="15" cy="13.5" r="1.6" fill="#8cc027"/></svg>
    <span><b>CART:</b> 0 item(s) - $0.00</span>
  </div>
  <nav class="abs nav">
    <a class="home">Home</a><a class="about">About</a><a class="store">Store</a><a class="featured">Featured</a><a class="news">News</a><a class="contacts">Contacts</a>
  </nav>
</header>

<main>
  <div class="abs panel"></div>

  <div class="abs slider" role="img" aria-label="Banner photo: a cheerful scientist and a child assembling a clock kit, with a price tag"></div>
  <div class="abs slider-stripe" role="img" aria-label="Green stripe across the top of the banner"></div>
  <div class="abs slider-arrow" style="left:270px"><svg width="8" height="10"><path d="M6 1L2 5l4 4" fill="none" stroke="#fff" stroke-width="2"/></svg></div>
  <div class="abs slider-arrow" style="left:686px"><svg width="8" height="10"><path d="M2 1l4 4-4 4" fill="none" stroke="#fff" stroke-width="2"/></svg></div>
  <div class="abs fold left"></div>
  <div class="abs fold right"></div>

  <form class="abs search">
    <h2>Advanced Search</h2>
    <div class="select" style="top:40px">Please select age...</div>
    <div class="gender"><span>◯ Boys</span><span>◯ Girls</span><span>✓ Both</span></div>
    <div class="ticks"><span>0</span><span>25</span><span>50</span><span>75</span><span>100</span><span>125</span><span>150</span><span>175</span><span>200</span></div>
    <div class="range"><span class="knob" style="left:0"></span><span class="knob" style="right:0"></span></div>
    <div class="range-val">min. € 0.0 - max. € 200.0</div>
    <div class="sep" style="top:168px"></div>
    <div class="select" style="top:174px">Please select category...</div>
    <div class="sep" style="top:203px"></div>
    <div class="submit">SUBMIT</div>
  </form>

  <h2 class="abs section-title" style="left:297px;top:460px">New Products</h2>

  <div class="abs product" style="left:297px;top:491px">
    <div class="product-img" role="img" aria-label="Product photo: baby playing with a toy laptop"></div>
    <div class="product-title">CRANE-DOWELL-LAUGH</div>
    <p class="product-desc">All toys are well-designed and we are sure that your kids...</p>
    <div class="product-buy"><span class="price">$360.00</span><span class="to-cart">ADD TO CART</span></div>
  </div>
  <div class="abs product" style="left:449px;top:491px">
    <div class="product-img" role="img" aria-label="Product photo: baby playing with a toy laptop"></div>
    <div class="product-title">CRANE-DOWELL-LAUGH</div>
    <p class="product-desc">All toys are well-designed and we are sure that your kids...</p>
    <div class="product-buy"><span class="price">$360.00</span><span class="to-cart">ADD TO CART</span></div>
  </div>
  <div class="abs product" style="left:600px;top:491px">
    <div class="product-img" role="img" aria-label="Product photo: baby playing with a toy laptop"></div>
    <div class="product-title">CRANE-DOWELL-LAUGH</div>
    <p class="product-desc">All toys are well-designed and we are sure that your kids...</p>
    <div class="product-buy"><span class="price">$360.00</span><span class="to-cart">ADD TO CART</span></div>
  </div>
  <div class="abs product" style="left:751px;top:491px">
    <div class="product-img" role="img" aria-label="Product photo: baby playing with a toy laptop"></div>
    <div class="product-title">CRANE-DOWELL-LAUGH</div>
    <p class="product-desc">All toys are well-designed and we are sure that your kids...</p>
    <div class="product-buy"><span class="price">$360.00</span><span class="to-cart">ADD TO CART</span></div>
  </div>

  <h2 class="abs section-title" style="left:297px;top:740px">Our Brands</h2>
  <div class="abs brand-tile plunex" style="left:300px">Plunex</div>
  <div class="abs brand-tile bruk" style="left:404px">BRUK</div>
  <div class="abs brand-tile crane" style="left:500px">Crane-Dowell</div>
  <div class="abs brand-tile plunex" style="left:604px">Plunex</div>
  <div class="abs brand-tile bruk" style="left:707px">BRUK</div>
  <div class="abs brand-tile crane" style="left:804px">Crane-Dowell</div>
  <div class="abs brand-arrow" style="left:305px"><svg width="8" height="10"><path d="M6 1L2 5l4 4" fill="none" stroke="#fff" stroke-width="2"/></svg></div>
  <div class="abs brand-arrow" style="left:870px"><svg width="8" height="10"><path d="M2 1l4 4-4 4" fill="none" stroke="#fff" stroke-width="2"/></svg></div>
</main>

<footer class="abs footer">
  <div class="foot-col" style="left:25px">
    <h3>Your Account</h3>
    <ul><li>Your Account</li><li>Personal information</li><li>Addresses</li><li>Discount</li><li>Order history</li></ul>
  </div>
  <div class="foot-col" style="left:176px">
    <h3>Our Offers</h3>
    <ul><li>New products</li><li>Top sellers</li><li>Specials</li><li>Manufacturers</li><li>Suppliers</li></ul>
  </div>
  <div class="foot-col" style="left:327px">
    <h3>Information</h3>
    <ul><li>Contact</li><li>Delivery</li><li>Legal Notice</li><li>Terms and conditions</li><li>About us</li></ul>
  </div>
  <div class="social"><span class="chirply">Chirply</span><span class="friendo">Friendo</span><span class="vidlane">Vidlane</span></div>
</footer>
<div class="abs bottom">©2014 Delvik™. All rights reserved</div>

</body>
</html>
```